Menu Board 1000mmx500mm re-design

I would like to re-design exiting menu board 1000mmx500mm. Current board letters are bit to small to read. I would like to have pictures (attached) of the food offered on it and at the same time to create balance between pictures and size of the text to be easily readable. Fonts and colours are up to designer choice but prefer warm and bright colours rather anything dark.

Target Market(s)

Food industry

Industry/Entity Type

Food

Font styles to use
Other font styles liked:
• I leave font choice to designer

Colors
FFC000
F8CF3A
FAE287
FDF2CF
FEFAEE
F0912C
F2A743
F7CA91
FBE8D2
FDF5EE
EE7325
F08F49
F5BC92
FAE3D3
FDF4ED

Requirements
Must have
• Pictures + Text
Nice to have
• Balance between images and text.
Should not have
• Can't think of any

```html
<!DOCTYPE html>
<html lang="en">
<head>
<meta charset="utf-8">
<title>Menu Board</title>
<link rel="stylesheet" href="https://fonts.googleapis.com/css2?family=Permanent+Marker&family=Montserrat:wght@400;500;700;800&family=Oswald:wght@600&display=swap">
<style>
  :root {
    --stage: #c8c8c8;
    --paper: #f3f3f4;
    --ink: #0a0a0a;
    --text: #2a2a2a;
    --orange: #f5851f;
    --red: #e8262a;
    --white: #ffffff;
  }
  * { box-sizing: border-box; margin: 0; padding: 0; }
  html, body { width: 713px; height: 1200px; overflow: hidden; background: var(--stage); }
  body { font-family: "Montserrat", sans-serif; color: var(--text); }

  .board {
    position: absolute; left: 56px; top: 0; width: 600px; height: 1200px;
    background: linear-gradient(120deg, #f7f7f8, #ececee 50%, #f7f7f8);
    overflow: hidden;
  }
  .board-top { position: absolute; left: 0; top: 0; width: 600px; height: 580px; }
  .board-foot { position: absolute; left: 0; top: 1060px; width: 600px; height: 140px; }

  .title {
    position: absolute; left: 0; right: 0; top: 40px; text-align: center;
    font-family: "Permanent Marker", cursive; font-size: 150px; line-height: 150px;
    color: var(--white); letter-spacing: -4px; transform: skewX(-4deg);
  }

  .photo-ring {
    position: absolute; border-radius: 50%; border: 7px solid var(--orange);
    padding: 6px; background: transparent;
  }
  .photo-ring.red { border-color: var(--red); }
  .photo { width: 100%; height: 100%; border-radius: 50%; }
  .photo.wrap { background: radial-gradient(circle at 45% 45%, #e9e1cf, #c9a98a 60%, #8d6a48); }
  .photo.beet { background: radial-gradient(circle at 50% 45%, #e9c7b8, #7a9c4e 45%, #a03a4c 80%); }
  .photo.chicken { background: radial-gradient(circle at 65% 45%, #f3f0e2, #d8b274 45%, #6e4a2e 85%); }
  .photo.ciabatta { background: radial-gradient(circle at 50% 50%, #d29a5a, #e9e4dc 55%, #f4f4f4); }
  .photo.potato { background: radial-gradient(circle at 50% 50%, #f2c34a, #d88b2a 60%, #8d5a1e); }

  .price {
    position: absolute; width: 48px; height: 48px; margin: -24px 0 0 -24px;
    border-radius: 50%; background: var(--red); color: var(--white);
    font-weight: 800; font-size: 17px; display: flex; align-items: center; justify-content: center;
  }
  .price::before {
    content: ""; position: absolute; left: 2px; top: -9px; width: 12px; height: 12px;
    border: 2px solid #5a1d1d; border-radius: 50%; border-right-color: transparent; border-bottom-color: transparent;
  }

  .pointer { position: absolute; width: 12px; margin-left: -6px; }
  .item-name {
    position: absolute; width: 170px; margin-left: -85px; text-align: center;
    color: var(--orange); font-weight: 800; font-size: 13.5px; letter-spacing: 0.2px;
  }
  .item-desc {
    position: absolute; width: 160px; margin-left: -80px; text-align: center;
    font-size: 12.5px; line-height: 16.3px; font-weight: 500; color: var(--text);
  }

  .drink-band {
    position: absolute; top: 1023px; height: 31px; background: var(--ink); color: var(--white);
    font-weight: 800; font-size: 16px; display: flex; align-items: center; justify-content: center;
    letter-spacing: 0.5px;
  }
  .drink-photo { position: absolute; border-radius: 6px; }
  .drink-photo.water { background: linear-gradient(90deg, #bcdcf0, #e8f4fb, #9fcbe8); }
  .drink-photo.cans { background: linear-gradient(90deg, #e6e6e6, #ffffff, #dcdcdc); }

  .sauces-title {
    position: absolute; left: 41px; top: 1106px; font-family: "Oswald", sans-serif;
    font-weight: 600; font-size: 64px; line-height: 70px; color: var(--white); letter-spacing: -1px;
  }
  .sauce {
    position: absolute; height: 21px; border-radius: 11px; background: var(--white); color: var(--ink);
    font-weight: 700; font-size: 12px; display: flex; align-items: center; justify-content: center;
  }
</style>
</head>
<body>
<main class="board">
  <svg class="board-top" viewBox="0 0 600 580" aria-hidden="true">
    <path fill="#0a0a0a" d="M0 0H600V505l-6-8-4 14-5-6-3 12-8-6-20 10-60-10-100-6-90 20-60 8-60 14-80 6-40 4-20 10-8-10-6 16-4-6-6 12-8-6-10 8V0z"/>
  </svg>
  <h1 class="title">MENU</h1>

  <div class="photo-ring" style="left:4px;top:221px;width:204px;height:204px;"><div class="photo wrap" role="img" aria-label="Grilled chicken wrap cut in half"></div></div>
  <div class="photo-ring red" style="left:162px;top:243px;width:270px;height:270px;"><div class="photo beet" role="img" aria-label="Beetroot wrap with chicken and salad"></div></div>
  <div class="photo-ring" style="left:381px;top:329px;width:212px;height:212px;"><div class="photo chicken" role="img" aria-label="Roast chicken with veggie rice"></div></div>

  <!-- Ciabatta -->
  <div class="photo-ring" style="left:61px;top:553px;width:108px;height:108px;border-width:5px;padding:4px;"><div class="photo ciabatta" role="img" aria-label="Chicken ciabatta sandwich"></div></div>
  <div class="price" style="left:181px;top:648px;">£6</div>
  <svg class="pointer" style="left:126px;top:670px;" viewBox="0 0 12 12" aria-hidden="true"><path d="M0 1h12L6 11z" fill="#0a0a0a"/></svg>
  <p class="item-name" style="left:126px;top:686px;">CIABATTA</p>
  <p class="item-desc" style="left:126px;top:708px;">Roti Chicken, Rucola, Caramelized Onions, Tomato, Fresh Onion</p>

  <!-- Quarter chicken -->
  <p class="item-name" style="left:306px;top:551px;">1/4 CHICKEN BOX</p>
  <p class="item-desc" style="left:306px;top:575px;">Roti Chicken, Veggie Rice &amp; Salad</p>
  <svg class="pointer" style="left:306px;top:612px;" viewBox="0 0 12 12" aria-hidden="true"><path d="M0 11h12L6 1z" fill="#0a0a0a"/></svg>
  <div class="photo-ring" style="left:234px;top:641px;width:108px;height:108px;border-width:5px;padding:4px;"><div class="photo chicken" role="img" aria-label="Quarter roast chicken with veggie rice"></div></div>
  <div class="price" style="left:355px;top:733px;">£9</div>

  <!-- Wrap -->
  <div class="photo-ring" style="left:408px;top:553px;width:108px;height:108px;border-width:5px;padding:4px;"><div class="photo wrap" role="img" aria-label="Grilled chicken wrap"></div></div>
  <div class="price" style="left:528px;top:648px;">£7</div>
  <svg class="pointer" style="left:480px;top:670px;" viewBox="0 0 12 12" aria-hidden="true"><path d="M0 1h12L6 11z" fill="#0a0a0a"/></svg>
  <p class="item-name" style="left:480px;top:686px;">WRAP</p>
  <p class="item-desc" style="left:480px;top:708px;">Roti Chicken, Crunchy Slaw, Tomato,Fresh Onion &amp; Sauce of your choice</p>

  <!-- Beetroot wrap -->
  <p class="item-name" style="left:306px;top:773px;">BEETROOT WRAP</p>
  <p class="item-desc" style="left:306px;top:794px;">Roti Chicken, Crunchy Slaw, Tomato, Fresh Onion &amp; Sauce of your choice</p>
  <svg class="pointer" style="left:306px;top:862px;" viewBox="0 0 12 12" aria-hidden="true"><path d="M0 11h12L6 1z" fill="#0a0a0a"/></svg>
  <div class="photo-ring" style="left:234px;top:889px;width:108px;height:108px;border-width:5px;padding:4px;"><div class="photo beet" role="img" aria-label="Beetroot wrap halves"></div></div>
  <div class="price" style="left:355px;top:984px;">£8</div>

  <!-- Roasted potatoes -->
  <div class="photo-ring" style="left:50px;top:793px;width:108px;height:108px;border-width:5px;padding:4px;"><div class="photo potato" role="img" aria-label="Roasted potatoes with thyme"></div></div>
  <div class="price" style="left:169px;top:887px;">£2.5</div>
  <svg class="pointer" style="left:120px;top:907px;" viewBox="0 0 12 12" aria-hidden="true"><path d="M0 1h12L6 11z" fill="#0a0a0a"/></svg>
  <p class="item-name" style="left:120px;top:923px;">ROASTED POTATOES</p>
  <p class="item-desc" style="left:120px;top:946px;">Thyme &amp; Garlic</p>

  <!-- Half chicken -->
  <div class="photo-ring" style="left:414px;top:793px;width:108px;height:108px;border-width:5px;padding:4px;"><div class="photo chicken" role="img" aria-label="Half roast chicken with veggie rice"></div></div>
  <div class="price" style="left:534px;top:888px;">£14</div>
  <svg class="pointer" style="left:479px;top:908px;" viewBox="0 0 12 12" aria-hidden="true"><path d="M0 1h12L6 11z" fill="#0a0a0a"/></svg>
  <p class="item-name" style="left:468px;top:924px;">1/2 CHICKEN BOX</p>
  <p class="item-desc" style="left:468px;top:947px;">Roti Chicken, Veggie Rice &amp; Salad</p>

  <!-- Footer -->
  <svg class="board-foot" viewBox="0 0 600 140" aria-hidden="true">
    <path fill="#f5851f" d="M0 18l6-6 4 8 6-10 5 6 8-4 10 6 20-4 40 4 60-2 80 4 60-4 60 2 80-6 50 4 30-6 20 0 12-10 6 6 4-8 6 6 3-8V140H0z"/>
  </svg>

  <div class="drink-photo water" style="left:26px;top:984px;width:56px;height:108px;" role="img" aria-label="Two bottles of mineral water"></div>
  <div class="drink-band" style="left:79px;width:132px;">WATER</div>
  <div class="price" style="left:232px;top:1045px;">£1</div>

  <div class="drink-photo cans" style="left:277px;top:1012px;width:72px;height:88px;" role="img" aria-label="Apple juice cans"></div>
  <div class="drink-band" style="left:349px;width:163px;">CAN &amp; JUICES</div>
  <div class="price" style="left:527px;top:1045px;">£1.8</div>

  <h2 class="sauces-title">SAUCES</h2>
  <span class="sauce" style="left:228px;top:1120px;width:128px;">SIGNATURE</span>
  <span class="sauce" style="left:360px;top:1120px;width:89px;">BBQ</span>
  <span class="sauce" style="left:454px;top:1120px;width:110px;">PIRI PIRI</span>
  <span class="sauce" style="left:228px;top:1145px;width:163px;">SWEET CHILLI</span>
  <span class="sauce" style="left:395px;top:1145px;width:169px;">GARLIC MAYO</span>
</main>
</body>
</html>
```